Business Card Design for new social media business

I am looking for a new professional business card design for an exciting new company which is based on providing members with experiences of others to benefit their choice of places to visit for restaurants, bars, clubs, national monument, tourist sights, hotels and so forth.
Updates

Please submit designs as I will choose to commit the funds depending on designs.

Reason: More designs required

Target Market(s)

Business Managers as well as directors alongside owners

Industry/Entity Type

Business

Requirements
Must have
• Logo design and symbols
Nice to have
• Logo / Symbol on the back of the business card and possibly the logo as if embedded/embossed on the business card.

```html
<!DOCTYPE html>
<html lang="en">
<head>
<meta charset="utf-8">
<title>Roamnote business card</title>
<link href="https://fonts.googleapis.com/css2?family=Jost:wght@300;400;500&display=swap" rel="stylesheet">
<style>
  :root {
    --page: #d9d9d9;
    --card-dark: #0b0b0b;
    --card-mid: #1e1e1e;
    --emboss: #2a2a2a;
    --name: #e6e6e6;
    --value: #d4d4d4;
    --label: #7fb0d6;
    --divider: #3a3a3a;
  }
  * { margin: 0; padding: 0; box-sizing: border-box; }
  html, body { width: 1200px; height: 1152px; overflow: hidden; }
  body {
    background: var(--page);
    font-family: "Jost", sans-serif;
    display: flex;
    flex-direction: column;
    align-items: center;
    justify-content: center;
    gap: 24px;
  }
  .card {
    position: relative;
    width: 960px;
    height: 540px;
    background: radial-gradient(ellipse at 50% 30%, var(--card-mid) 0%, var(--card-dark) 70%);
    overflow: hidden;
  }
  .brand {
    position: absolute;
    display: flex;
    flex-direction: column;
    align-items: flex-start;
    color: var(--emboss);
    font-weight: 500;
  }
  .brand-row { display: flex; align-items: center; gap: 28px; }
  .brand-dot {
    width: 120px; height: 120px;
    border-radius: 50%;
    background: var(--emboss);
  }
  .brand-name { font-size: 150px; line-height: 1; letter-spacing: -2px; }
  .brand-tagline {
    font-size: 30px;
    font-weight: 500;
    letter-spacing: 16px;
    margin-left: 150px;
    margin-top: 6px;
  }
  .card-back .brand { left: 130px; top: 170px; }
  .card-front .brand { left: 200px; top: 330px; transform: scale(0.85); transform-origin: left top; }
  .holder {
    position: absolute;
    right: 520px;
    top: 222px;
    text-align: right;
  }
  .holder-name { font-size: 44px; font-weight: 400; color: var(--name); line-height: 1.1; }
  .holder-title { font-size: 21px; font-weight: 300; color: var(--value); margin-top: 4px; }
  .divider {
    position: absolute;
    left: 460px;
    top: 168px;
    width: 1px;
    height: 156px;
    background: var(--divider);
  }
  .contacts {
    position: absolute;
    left: 478px;
    top: 162px;
    list-style: none;
    font-size: 19px;
    line-height: 32px;
    color: var(--value);
  }
  .contacts .label { color: var(--label); font-style: italic; font-weight: 400; }
</style>
</head>
<body>
  <section class="card card-back" aria-label="Card back">
    <div class="brand">
      <div class="brand-row">
        <span class="brand-dot"></span>
        <span class="brand-name">Roamnote</span>
      </div>
      <span class="brand-tagline">your business tagline</span>
    </div>
  </section>

  <section class="card card-front" aria-label="Card front">
    <div class="brand">
      <div class="brand-row">
        <span class="brand-dot"></span>
        <span class="brand-name">Roamnote</span>
      </div>
      <span class="brand-tagline">your business tagline</span>
    </div>
    <div class="holder">
      <p class="holder-name">Mira Castell</p>
      <p class="holder-title">head manager</p>
    </div>
    <div class="divider"></div>
    <ul class="contacts">
      <li><span class="label">address:</span> 118 Harbor Lane, Eastfield NY 10432</li>
      <li><span class="label">telephone:</span> 020 555 0147</li>
      <li><span class="label">email:</span> miracastell@roamnote.com</li>
      <li><span class="label">website:</span> www.roamnote.com</li>
      <li><span class="label">social:</span> www.social.example/roamnote</li>
    </ul>
  </section>
</body>
</html>
```